Real Estate Agent Service Brochure

I need a trifold brochure to showcase my real estate services. I am a veteran Real Estate Broker specializing in marketing properties for sale and for top dollar. I would like to see designs that use colors from my logo (attached) and I would like to showcase some before and after photos of staging jobs I have done to homes to get them ready for the market. This brochure is specific to home sellers. You are happy to go check out my website for inspiration www.lomavertpa.com but keep the copy as I have written it. The the final design should communicate experienced professional who uses current technologies and strategies to market properties for the highest value.

Target Market(s)

Homeowners wanting to sell their homes

Industry/Entity Type

Real Estate Agent

Font styles to use
Serif

Requirements
Must have
• My, logo, personal photo, title and contact information as listed:
• Marta Venholt
• Owner Broker
• Stager Re-Designer
• 860-912-7048
• BRAVE Realty LLC
• LOMAVERTPA.com
• Marta@LOMAVERTPA.com
• The colors used should be those in my logo.
• Brochure should be able to fit in standard envelope for mailing.
Nice to have
• I think I would like my personal photo and contact information on the front panel.
Should not have
• Bright colors.

```html
<!DOCTYPE html>
<html lang="en">
<head>
<meta charset="utf-8">
<title>BRAVE Realty LLC – Seller Brochure</title>
<link rel="stylesheet" href="https://fonts.googleapis.com/css2?family=Open+Sans:ital,wght@0,400;0,600;0,700;1,400;1,700&display=swap">
<style>
:root{
  --backdrop:#4a4a4c;
  --navy:#14355d;
  --navy-deep:#0f2a4b;
  --blue-mid:#2b5b8a;
  --paper:#f3f4f5;
  --paper-shade:#dfe1e4;
  --wave-grey:#c9cbcf;
  --ink:#2e3440;
  --white:#ffffff;
}
*{box-sizing:border-box;margin:0;padding:0}
html,body{width:1200px;height:874px;overflow:hidden;background:var(--backdrop);font-family:"Open Sans",Arial,sans-serif;color:var(--ink)}
.canvas{position:relative;width:1200px;height:874px}

.panel{position:absolute;background:linear-gradient(180deg,var(--paper),var(--paper-shade));overflow:hidden}
.wave{position:absolute;left:0;top:0;width:100%;height:100%}

/* Logo */
.brand{display:flex;align-items:center;justify-content:center;gap:7px;color:var(--navy);font-weight:700;letter-spacing:.06em}
.brand-mark{width:11px;height:11px;background:var(--navy)}
.brand-name{font-size:20px}

/* Contacts */
.contacts{list-style:none;color:var(--white);font-size:11.5px;font-style:italic}
.contacts li{display:flex;align-items:center;gap:6px;margin-bottom:3px}
.contacts svg{width:11px;height:11px;flex:none}

/* Photo placeholders */
.photo{position:absolute}
.photo-house{background:linear-gradient(180deg,#8a8fb8 0%,#c9b7c4 40%,#3c4a66 75%,#556b45 100%)}
.photo-agent{background:linear-gradient(180deg,#c4c6c8,#8e9196 60%,#2a2d33)}
.photo-kitchen{background:linear-gradient(135deg,#efe6d6,#b59a74 55%,#5e4a35)}
.photo-living-before{background:linear-gradient(135deg,#d9d0c2,#8a7766 60%,#4c3d33)}
.photo-living-after{background:linear-gradient(135deg,#f4efe6,#c8b9a3 55%,#7d6b58)}
.photo-floor-before{background:linear-gradient(135deg,#e6e2db,#a89c8e 55%,#5b5047)}
.photo-floor-after{background:linear-gradient(135deg,#f3ede3,#b8a486 55%,#6a5943)}

.photo-label{position:absolute;font-size:11.5px;font-weight:600;color:var(--navy)}

/* Cover */
.cover{left:40px;top:112px;width:270px;height:650px}
.cover .brand{position:absolute;top:26px;left:0;width:100%}
.cover .photo-house{left:0;top:72px;width:270px;height:175px}
.cover .photo-agent{left:160px;top:150px;width:110px;height:165px}
.agent-tag{position:absolute;left:160px;top:315px;width:110px;background:var(--navy);color:var(--white);padding:5px 7px;font-size:9px;line-height:1.45}
.agent-tag .agent-name{font-weight:700;font-style:italic}
.cover-copy{position:absolute;left:18px;top:262px;width:134px;font-style:italic;font-size:10px;line-height:1.4;text-align:right}
.cover-copy .lead{font-weight:700;margin-bottom:6px}
.cover .contacts{position:absolute;left:70px;top:502px}

/* Inside spread */
.spread{left:330px;top:112px;width:830px;height:650px}
.column{position:absolute;top:0;width:276px;height:100%}
.col-1{left:0}.col-2{left:277px}.col-3{left:554px}
.fold{position:absolute;top:0;width:1px;height:100%;background:rgba(0,0,0,.08)}
.copy{position:absolute;left:18px;width:240px;font-size:9.3px;line-height:1.45}
.copy p{margin-bottom:7px}
.copy .by{font-weight:700;font-style:italic}
.navy-copy{position:absolute;left:18px;width:240px;color:var(--white);font-size:9.6px;line-height:1.5}
.col-3 .brand{position:absolute;top:352px;left:0;width:100%}
.col-3 .contacts{position:absolute;left:80px;top:478px}
</style>
</head>
<body>
<main class="canvas">

  <!-- Front cover -->
  <section class="panel cover" aria-label="Front cover">
    <svg class="wave" viewBox="0 0 270 650" preserveAspectRatio="none" aria-hidden="true">
      <path d="M0,410 C90,395 180,398 270,385 L270,650 L0,650Z" fill="var(--wave-grey)"/>
      <path d="M0,440 C90,425 180,428 270,415 L270,650 L0,650Z" fill="var(--navy)"/>
    </svg>
    <div class="brand"><span class="brand-mark"></span><span class="brand-name">BRAVE REALTY LLC</span></div>
    <div class="photo photo-house" role="img" aria-label="Photo of a two-storey house at dusk"></div>
    <div class="photo photo-agent" role="img" aria-label="Portrait of Marta Venholt"></div>
    <div class="agent-tag">
      <div class="agent-name">Marta Venholt</div>
      <div>· Owner Broker</div>
      <div>· Stage Re-Designer</div>
    </div>
    <div class="cover-copy">
      <p class="lead">A home is one of your most valuable assets.</p>
      <p>If you are thinking about selling a property, it is crucial that you hire someone with an extraordinary history of happy sellers.</p>
    </div>
    <ul class="contacts">
      <li><svg viewBox="0 0 12 12"><circle cx="6" cy="6" r="6" fill="#fff"/><path d="M4 3.2l1 1.2-.6.8c.4.9 1 1.5 1.9 1.9l.8-.6 1.2 1-.6 1.1c-2 .1-4.4-2.3-4.3-4.3z" fill="var(--navy)"/></svg>860-912-7048</li>
      <li><svg viewBox="0 0 12 12"><circle cx="6" cy="6" r="6" fill="#fff"/><circle cx="6" cy="6" r="3.3" fill="none" stroke="var(--navy)" stroke-width=".8"/><path d="M2.7 6h6.6M6 2.7v6.6" stroke="var(--navy)" stroke-width=".7"/></svg>lomavertpa.com</li>
      <li><svg viewBox="0 0 12 12"><circle cx="6" cy="6" r="6" fill="#fff"/><rect x="3" y="4" width="6" height="4.2" fill="none" stroke="var(--navy)" stroke-width=".8"/><path d="M3 4l3 2.3L9 4" fill="none" stroke="var(--navy)" stroke-width=".8"/></svg>marta@lomavertpa.com</li>
    </ul>
  </section>

  <!-- Inside spread -->
  <section class="panel spread" aria-label="Inside spread">
    <svg class="wave" viewBox="0 0 830 650" preserveAspectRatio="none" aria-hidden="true">
      <path d="M0,420 C220,395 560,410 830,378 L830,650 L0,650Z" fill="var(--wave-grey)"/>
      <path d="M0,448 C220,423 560,438 830,406 L830,650 L0,650Z" fill="var(--navy)"/>
    </svg>
    <span class="fold" style="left:276px"></span>
    <span class="fold" style="left:553px"></span>

    <div class="column col-1">
      <div class="copy" style="top:34px">
        <p>When you work with Marta you gain a partner who cares for all the details, so that your home sells quickly and for the best price.</p>
        <p>Marta is knowledgeable and professional. Having worked with three separate real estate agents, she is by far the best broker. I am always impressed by her negotiating skills, her attention to detail and her ability to manage the entire process.</p>
      </div>
      <span class="photo-label" style="left:150px;top:300px">Kitchen After</span>
      <div class="photo photo-kitchen" style="left:0;top:320px;width:276px;height:95px" role="img" aria-label="Staged kitchen after photo"></div>
      <p class="navy-copy" style="top:478px">Marta devotes her efforts to selling real estate, by keeping up with the evolving market, researching buyer trends and preparing homes before they enter the market by staging them to connect with the target buyer. Marta knows all sales are not alike. Therefore, taking a cookie cutter approach is not acceptable, she recognizes that each property is unique and requires a personalized marketing plan and strategy.</p>
    </div>

    <div class="column col-2">
      <div class="copy" style="top:34px">
        <p>The marketing and staging of our house was on point, I don't think the sale of our home would have been as successful without it.</p>
        <p class="by">Paul &amp; Ines R.</p>
        <p>I have had several real estate dealings with Marta each one was handled professionally and with my best interest in mind. Her marketing skills are top notch she made sure my properties where ready for market and showcased them in the best way by staging them and having professional photography done. She helped me get through home inspections issues keeping the sales in tact. I keep using her services and recommend her to family and friends she really knows her stuff!</p>
        <p class="by">Odile K.</p>
      </div>
      <span class="photo-label" style="left:10px;top:300px">Living Room Before</span>
      <span class="photo-label" style="left:148px;top:290px">Living Room After</span>
      <div class="photo photo-living-before" style="left:0;top:318px;width:138px;height:95px" role="img" aria-label="Living room before staging"></div>
      <div class="photo photo-living-after" style="left:138px;top:308px;width:138px;height:105px" role="img" aria-label="Living room after staging"></div>
      <p class="navy-copy" style="top:462px">A veteran in the real estate industry with nearly 30 years expertise and consistent membership in the Multi-Million-Dollar Club combined with her HSA Home Stager and Re-Designer credentials assures that her clients get the advantage of vast knowledge, seasoned experience and proven results, all geared to creating beautiful spaces, which form a connection with the right buyer producing the highest and best offer.</p>
    </div>

    <div class="column col-3">
      <div class="copy" style="top:34px">
        <p>Marta directed us right from the beginning by preparing a market evaluation using current data, helping us to establish a proper list price; she prepared our property for the market by staging it and then marketed it with great photography and video tours. Because of her pre-marketing preparations we received several offers on our house! Keeping our interests first, Marta negotiated the best deal for us; we were truly blown away by her knowledge, work ethic and professionalism.</p>
        <p class="by">Ray &amp; Lena T</p>
      </div>
      <span class="photo-label" style="left:14px;top:228px">1st Floor Before</span>
      <span class="photo-label" style="left:160px;top:190px">1st Floor After</span>
      <div class="photo photo-floor-before" style="left:0;top:246px;width:138px;height:82px" role="img" aria-label="First floor before staging"></div>
      <div class="photo photo-floor-after" style="left:138px;top:208px;width:138px;height:120px" role="img" aria-label="First floor after staging"></div>
      <div class="brand"><span class="brand-mark"></span><span class="brand-name">BRAVE REALTY LLC</span></div>
      <ul class="contacts">
        <li><svg viewBox="0 0 12 12"><circle cx="6" cy="6" r="6" fill="#fff"/><path d="M4 3.2l1 1.2-.6.8c.4.9 1 1.5 1.9 1.9l.8-.6 1.2 1-.6 1.1c-2 .1-4.4-2.3-4.3-4.3z" fill="var(--navy)"/></svg>860-912-7048</li>
        <li><svg viewBox="0 0 12 12"><circle cx="6" cy="6" r="6" fill="#fff"/><circle cx="6" cy="6" r="3.3" fill="none" stroke="var(--navy)" stroke-width=".8"/><path d="M2.7 6h6.6M6 2.7v6.6" stroke="var(--navy)" stroke-width=".7"/></svg>lomavertpa.com</li>
        <li><svg viewBox="0 0 12 12"><circle cx="6" cy="6" r="6" fill="#fff"/><rect x="3" y="4" width="6" height="4.2" fill="none" stroke="var(--navy)" stroke-width=".8"/><path d="M3 4l3 2.3L9 4" fill="none" stroke="var(--navy)" stroke-width=".8"/></svg>marta@lomavertpa.com</li>
      </ul>
    </div>
  </section>

</main>
</body>
</html>
```